We need a company profile design 8 + cover

The company profile is attached below, we need to renew the whole thing with full modification. content and page arrangement is the same. All should be A5 size printable and electronic copies.

I attached logo and colors for identity, please use logo colors as main scheme colours

We need 2 copies Arabic and English

Font styles to use
Sans Serif

Requirements
Nice to have
• Please let us know how we can use the designs to edit in Arabic

```html
<!DOCTYPE html>
<html lang="en">
<head>
<meta charset="utf-8">
<title>Education Level – Company Profile Spread</title>
<link rel="stylesheet" href="https://fonts.googleapis.com/css2?family=Source+Sans+3:wght@400;600;700&display=swap">
<style>
  :root {
    --stage: #d7d8db;
    --paper: #ffffff;
    --navy: #1f3567;
    --navy-title: #3a4c7e;
    --tier-grey: #7c7d80;
    --tier-dark: #2a2a2d;
    --tier-light: #a9aaad;
    --ink-black: #161617;
    --photo-warm-1: #d9cdb6;
    --photo-warm-2: #8f8a80;
    --photo-grad-1: #5a4a45;
    --photo-grad-2: #b58f78;
    --photo-books-1: #c7a77a;
    --photo-books-2: #8d5b4a;
  }
  html, body {
    margin: 0;
    padding: 0;
    width: 1200px;
    height: 691px;
    overflow: hidden;
    background: var(--stage);
  }
  .spread {
    position: absolute;
    left: 30px;
    top: 144px;
    width: 1140px;
    height: 402px;
    background: var(--paper);
    box-shadow: 0 6px 18px rgba(0,0,0,.22);
    font-family: "Source Sans 3", sans-serif;
  }
  .spread svg { display: block; }
  .section-title {
    font-family: "Source Sans 3", sans-serif;
    font-weight: 600;
    font-size: 24px;
    fill: var(--navy-title);
  }
  .tier-label {
    font-family: "Source Sans 3", sans-serif;
    font-size: 10px;
    fill: #ffffff;
  }
  .tier-label .strong { font-weight: 700; }
  .tagline {
    font-family: "Source Sans 3", sans-serif;
    font-weight: 700;
    font-size: 12.5px;
    letter-spacing: .3px;
    fill: var(--navy);
  }
</style>
</head>
<body>
<div class="spread">
  <svg width="1140" height="402" viewBox="0 0 1140 402">
    <defs>
      <linearGradient id="studentsTone" x1="0" y1="0" x2="1" y2="1">
        <stop offset="0" stop-color="var(--photo-warm-1)"/>
        <stop offset="1" stop-color="var(--photo-warm-2)"/>
      </linearGradient>
      <linearGradient id="graduatesTone" x1="0" y1="0" x2="1" y2="1">
        <stop offset="0" stop-color="var(--photo-grad-2)"/>
        <stop offset="1" stop-color="var(--photo-grad-1)"/>
      </linearGradient>
      <linearGradient id="booksTone" x1="0" y1="0" x2="1" y2="1">
        <stop offset="0" stop-color="var(--photo-books-1)"/>
        <stop offset="1" stop-color="var(--photo-books-2)"/>
      </linearGradient>
      <linearGradient id="spineShade" x1="0" y1="0" x2="1" y2="0">
        <stop offset="0" stop-color="#000" stop-opacity="0"/>
        <stop offset=".5" stop-color="#000" stop-opacity=".14"/>
        <stop offset="1" stop-color="#000" stop-opacity="0"/>
      </linearGradient>
    </defs>

    <!-- left page imagery -->
    <polygon class="photo-students" role="img" aria-label="Photo of students studying and writing at a classroom table"
      points="0,0 700,0 470,402 0,402" fill="url(#studentsTone)"/>
    <line x1="0" y1="34" x2="318" y2="322" stroke="var(--paper)" stroke-width="8"/>
    <polygon class="photo-graduates" role="img" aria-label="Photo of smiling graduates in caps and gowns"
      points="0,42 304,318 150,402 0,402" fill="url(#graduatesTone)"/>
    <polygon class="accent-black" points="318,326 440,402 168,402" fill="var(--ink-black)"/>
    <line x1="304" y1="318" x2="150" y2="402" stroke="var(--paper)" stroke-width="6"/>

    <!-- navy accent across spine -->
    <line x1="700" y1="0" x2="470" y2="402" stroke="var(--paper)" stroke-width="5"/>
    <polygon class="accent-navy" points="470,402 534,290 740,402" fill="var(--navy)"/>

    <!-- books cutout -->
    <polygon class="photo-books" role="img" aria-label="Photo of students reading on a stack of books"
      points="606,132 672,124 700,176 684,228 620,236 594,186" fill="url(#booksTone)"/>

    <!-- spine -->
    <rect x="560" y="0" width="20" height="402" fill="url(#spineShade)"/>

    <!-- right page content -->
    <text class="section-title" x="890" y="46" text-anchor="middle">Education Level</text>

    <g class="pyramid">
      <!-- tabs -->
      <rect x="920" y="134" width="90" height="22" rx="11" fill="var(--navy)"/>
      <rect x="960" y="176" width="100" height="22" rx="11" fill="var(--tier-grey)"/>
      <rect x="1010" y="244" width="100" height="22" rx="11" fill="var(--tier-dark)"/>
      <rect x="1050" y="302" width="84" height="22" rx="11" fill="var(--tier-light)"/>

      <!-- tiers -->
      <polygon points="890,66 970,160 810,160" fill="var(--navy)"/>
      <polygon points="812,168 968,168 1022,228 758,228" fill="var(--tier-grey)"/>
      <polygon points="750,236 1030,236 1076,288 704,288" fill="var(--tier-dark)"/>
      <polygon points="696,296 1084,296 1122,340 658,340" fill="var(--tier-light)"/>

      <text class="tier-label" text-anchor="middle">
        <tspan class="strong" x="890" y="138">PHD /DBA</tspan>
        <tspan x="890" y="151">(3 - 4 Years)</tspan>
      </text>
      <text class="tier-label" text-anchor="middle">
        <tspan class="strong" x="890" y="182">Masters Degree</tspan>
        <tspan x="890" y="193">(1 to 2 Years)</tspan>
        <tspan x="890" y="204">MBA</tspan>
        <tspan x="890" y="215">(1 to 2 Years)</tspan>
      </text>
      <text class="tier-label" text-anchor="middle">
        <tspan x="890" y="259"><tspan class="strong">Undergraduate Degree</tspan> - Bachelors Degree</tspan>
        <tspan x="890" y="272">(3 - 4 Years)</tspan>
      </text>
      <text class="tier-label" text-anchor="middle">
        <tspan x="890" y="316"><tspan class="strong">Foundation / Pathway Cources</tspan>– English Language</tspan>
        <tspan x="890" y="329">(6 to 12 Months)</tspan>
      </text>
    </g>

    <text class="tagline" x="890" y="374" text-anchor="middle">WE ARE READY TO SERVE YOU '24 X 7'</text>
  </svg>
</div>
</body>
</html>
```